依頼詳細
屋外にタペストリーで掲げている店案内ですが、ショッピングセンター内にあるため屋外からエステだと一目でわかるものにしたいと考えております。そのためのデザインをお願いいたします。
記載項目
記載項目
特にエステティックであることをはっきりと掲載したいため「ロゴマーク」「エステティックサロン」「美顔」「痩身」「脱毛」というワードを大きく
続いて「電話番号」「営業時間」
また「店名」も掲載しますが目立たなくとも良いです。
ロゴマークは添付のものをご利用ください。
色ならびにロゴマーク中のグラデーションの変更はしないようにお願いいたします。
参考として旧タペストリーと他店の駐車場看板を添付します。
旧タペストリーのデザインとは全くかけ離れて構いません。
駐車場看板は見せ方の参考として添付します。店名よりもエステティックを強調しているという事の参考になればと思います。

店名 ルフィナ鯖江店
電話番号 0778-41-6093
営業時間 9:30~20:30
サイズ:縦2400mm×横3200mm
希望イメージ
シンプル 複雑
単色 カラフル
暗い 明るい
日常 高級
遊び心 厳粛
未来的 伝統的
女性的 男性的
希望する色
設定なし
納品ファイル
• イラストレーター形式 (.ai)
• フォトショップ形式 (.psd)
補足説明
写真利用の場合は、納品の際は埋め込みではなくリンクでお願いします。
表記につきまして若干変更をさせていただきます、

「エステティックサロン」は英字よりカナ表記が目立つようにお願いいたします。
「美顔」→「フェイシャル」に変更(カナ表記)
「痩身」→「ボディ」に変更(カナ表記)
「脱毛」→変更なし

また女性の画像等はイメージやパーツとして使用いただいてもOKですが、スワンのマークをもう少し前面に出していただけたらと思います。
画像のイメージが前面にでるより、スワンのロゴが前面にでるようにできればと思います。イメージ画像等は全くないものでも可です。

添付でスワンのロゴのみのaiを追加いたします。

締め切りを変更させていただきます。

当方が伝えたいものが、しっかりと出ていて、色味も落ち着きがありながらロゴがはっきりと見えるデザインで好感が持てました。

本当にたくさんのデザインを頂きありがとうございます。

```html
<!DOCTYPE html>
<html lang="ja">
<head>
<meta charset="utf-8">
<title>RUFINA エステティックサロン タペストリー</title>
<link rel="stylesheet" href="https://fonts.googleapis.com/css2?family=Fira+Sans+Condensed:wght@400&family=Zen+Kaku+Gothic+New:wght@400;500&family=Noto+Sans+JP:wght@400&display=swap">
<style>
  :root {
    --paper: #e7e4e5;
    --rose: #d6485a;
    --rose-soft: #e46a7a;
    --cocoa: #5b2b24;
    --ornament: #a98a86;
    --white: #ffffff;
  }
  html, body {
    margin: 0;
    padding: 0;
    width: 1200px;
    height: 900px;
    overflow: hidden;
    background: var(--paper);
  }
  .tapestry {
    display: block;
    width: 1200px;
    height: 900px;
  }
  .brand-tag,
  .brand-name {
    font-family: "Fira Sans Condensed", sans-serif;
    font-weight: 400;
    fill: var(--rose);
  }
  .menu-line {
    font-family: "Zen Kaku Gothic New", sans-serif;
    font-weight: 500;
    fill: var(--cocoa);
  }
  .store-name {
    font-family: "Zen Kaku Gothic New", sans-serif;
    font-weight: 500;
    fill: var(--white);
  }
  .salon-type {
    font-family: "Zen Kaku Gothic New", sans-serif;
    font-weight: 500;
    fill: var(--white);
  }
  .contact-line {
    font-family: "Noto Sans JP", sans-serif;
    font-weight: 400;
    fill: var(--white);
  }
</style>
</head>
<body>
<svg class="tapestry" viewBox="0 0 1200 900" xmlns="http://www.w3.org/2000/svg">
  <defs>
    <radialGradient id="brand-glow" cx="0.5" cy="0.5" r="0.5">
      <stop offset="0" stop-color="#ffffff" stop-opacity="0.9"/>
      <stop offset="1" stop-color="#ffffff" stop-opacity="0"/>
    </radialGradient>
  </defs>

  <rect class="damask-field" x="0" y="0" width="1200" height="594" fill="var(--paper)" role="img" aria-label="淡いグレーのダマスク柄の背景"/>
  <rect class="damask-band" x="0" y="594" width="1200" height="306" fill="var(--rose)" role="img" aria-label="ローズ色のダマスク柄の帯"/>

  <ellipse cx="260" cy="320" rx="290" ry="290" fill="url(#brand-glow)"/>
  <circle class="brand-dot" cx="250" cy="330" r="170" fill="var(--rose-soft)"/>

  <text class="brand-tag" x="512" y="114" font-size="38" textLength="256" lengthAdjust="spacingAndGlyphs">Esthetic salon</text>
  <text class="brand-name" x="516" y="228" font-size="100" textLength="456" lengthAdjust="spacingAndGlyphs">RUFINA</text>

  <rect class="ornament" x="480" y="279" width="528" height="5" rx="2.5" fill="var(--ornament)" role="img" aria-label="飾り罫"/>
  <rect class="ornament" x="480" y="526" width="528" height="5" rx="2.5" fill="var(--ornament)" role="img" aria-label="飾り罫"/>

  <text class="menu-line" x="540" y="372" font-size="66" textLength="420" lengthAdjust="spacingAndGlyphs">フェイシャル</text>
  <line x1="528" y1="400" x2="1002" y2="400" stroke="var(--cocoa)" stroke-width="2"/>
  <text class="menu-line" x="540" y="492" font-size="66" textLength="444" lengthAdjust="spacingAndGlyphs">ボディ・脱毛</text>

  <text class="store-name" x="744" y="660" font-size="30" text-anchor="middle" textLength="228" lengthAdjust="spacingAndGlyphs">ルフィナ鯖江店</text>
  <text class="salon-type" x="96" y="770" font-size="94" textLength="1038" lengthAdjust="spacingAndGlyphs">エステティックサロン</text>
  <text class="contact-line" x="114" y="852" font-size="44" textLength="1014" lengthAdjust="spacingAndGlyphs">TEL.0778-41-6093　OPEN 9:30～20:30</text>
</svg>
</body>
</html>
```